Consumer Facing Energy Data Analytics Startup Needs a Postcard to Promote New Product

We need a set of 2 postcards (6 x 4.25 inches as describers in the attached files) to help us promote our product for a new company based in San Francisco called "Lumo Crest".
We develop an alert platform for customers of energy utility companies. Our initial product is "Lumo Signal" - an application that helps people better manage their energy bill by sending an SMS or email alter in advance of a high bill.
We would like to see designs that use the colors blue and orange (same as in the website: www.lumocrest.example). The text of the postcards will be reworked once a layout has been chosen, but we welcome original ways to attract the customers' attention.
Our goal is ultimately to have our targets go the our website and sign up for our service.
The final deliverable should be 8 vector files (preferable .eps, 4 file types, one version in print and one in web format):
- front of card for our small and medium business customers
- front of card for our residential customers
- back of card for our small and medium business customers
- back of card for our residential customers
- DINPro and Avenir

```html
<!DOCTYPE html>
<html lang="en">
<head>
<meta charset="utf-8">
<title>Lumo Signal Postcard</title>
<link href="https://fonts.googleapis.com/css2?family=Barlow:wght@400;500&family=Nunito+Sans:wght@600;700;800&family=Lora:wght@400;700&display=swap" rel="stylesheet">
<style>
  :root {
    --blue: #29a8e0;
    --blue-deep: #3299cc;
    --blue-soft: #45b2e1;
    --orange: #f9ab3c;
    --white: #ffffff;
    --ink: #2b2b2b;
    --grey: #7a7a7a;
    --line: #e2e2e2;
    --backdrop: #dcdcdc;
  }
  * { box-sizing: border-box; margin: 0; padding: 0; }
  html, body { width: 1200px; height: 918px; overflow: hidden; background: var(--backdrop); }

  .postcard {
    position: absolute; left: 40px; top: 62px;
    width: 1120px; height: 793px;
    background: var(--blue);
    overflow: hidden;
    box-shadow: 0 4px 14px rgba(0,0,0,.25);
  }

  .intro-panel {
    position: absolute; left: 32px; top: 37px;
    width: 1058px; height: 203px;
    background: var(--white); border-radius: 28px;
    padding: 26px 0 0 32px;
    font-family: "Barlow", sans-serif; font-size: 19px; line-height: 25px; color: var(--ink);
  }
  .intro-panel p { width: 560px; }
  .intro-panel .lead { margin-bottom: 25px; }

  .alert-preview {
    position: absolute; left: 641px; top: 72px;
    width: 421px; height: 374px;
    background: var(--white);
    box-shadow: 0 1px 5px rgba(0,0,0,.18);
    font-family: "Nunito Sans", sans-serif;
  }
  .preview-badge {
    position: absolute; left: 196px; top: -14px;
    width: 28px; height: 28px; border-radius: 50%; background: var(--orange);
  }
  .preview-header {
    height: 37px; background: var(--blue-deep);
    color: var(--white); text-align: center;
    font-size: 10px; font-weight: 700; letter-spacing: 2px; padding-top: 19px;
  }
  .preview-status {
    height: 115px; background: var(--blue-soft); text-align: center; color: var(--white);
    padding-top: 12px;
    font-family: "Lora", serif;
  }
  .preview-status .risk { font-size: 11px; opacity: .9; }
  .preview-status .increase { font-size: 19px; margin-top: 2px; }
  .preview-status .increase strong { color: var(--orange); font-family: "Nunito Sans", sans-serif; font-size: 25px; font-weight: 800; }
  .cycle-pill {
    display: inline-block; margin-top: 8px;
    width: 199px; height: 27px; line-height: 27px;
    background: var(--white); border-radius: 4px;
    font-family: "Nunito Sans", sans-serif; font-size: 10px; color: var(--grey);
  }
  .cycle-pill strong { color: var(--orange); font-size: 15px; font-weight: 800; margin-right: 3px; }

  .preview-tips { padding: 14px 0 0; }
  .tips-heading { text-align: center; font-size: 12px; color: #555; margin-bottom: 12px; }
  .tips { display: flex; }
  .tip {
    flex: 1; text-align: center; padding: 4px 8px 0;
    border-right: 1px solid var(--line); height: 160px; position: relative;
  }
  .tip:last-child { border-right: none; }
  .tip-icon { width: 46px; height: 40px; margin: 0 auto 10px; background: #cfd6db; border-radius: 6px; }
  .tip-title { font-size: 8.5px; font-weight: 700; color: #555; margin-bottom: 7px; }
  .tip-body { font-size: 7.5px; line-height: 10px; color: var(--grey); }
  .tip-button {
    position: absolute; left: 50%; bottom: 6px; transform: translateX(-50%);
    width: 56px; height: 17px; line-height: 17px; background: var(--orange);
    color: var(--white); font-size: 7.5px; font-weight: 700; border-radius: 2px;
  }

  .benefit {
    position: absolute; left: 40px; width: 547px; height: 97px;
    background: var(--orange); border-radius: 49px;
    padding: 17px 0 0 30px;
    font-family: "Nunito Sans", sans-serif; font-weight: 700; font-size: 25px; line-height: 31px;
    color: var(--white);
  }
  .benefit:nth-of-type(1) { top: 267px; }
  .benefit:nth-of-type(2) { top: 383px; }
  .benefit:nth-of-type(3) { top: 499px; }
  .benefit:nth-of-type(4) { top: 615px; }

  .contact {
    position: absolute; left: 76px; top: 730px;
    display: flex; gap: 24px;
    font-family: "Nunito Sans", sans-serif; font-weight: 700; font-size: 24px; color: var(--white);
  }
  .contact span { display: flex; align-items: center; gap: 4px; }

  .brand-disc {
    position: absolute; left: 744px; top: 446px;
    width: 522px; height: 522px; border-radius: 50%; background: var(--white);
  }
  .brand-name {
    position: absolute; left: 770px; top: 700px; width: 340px; text-align: center;
    font-family: "Nunito Sans", sans-serif; font-weight: 700; font-size: 40px; letter-spacing: 2px;
    color: var(--blue);
  }
</style>
</head>
<body>
  <main class="postcard">
    <section class="intro-panel">
      <p class="lead">Lumo Crest helps you predict and avoid your high energy bills.</p>
      <p>Lumo Crest employs advanced analytics software to assess customer energy use on a daily basis. We predict monthly energy bills based on current usage, and provide customer alerts and tips when use is above normal.</p>
    </section>

    <section class="alert-preview">
      <div class="preview-badge"></div>
      <div class="preview-header">- LUMO SIGNAL -</div>
      <div class="preview-status">
        <p class="risk">You're at risk of a higher than average energy bill</p>
        <p class="increase">Bill increase from last month: <strong>30%</strong></p>
        <div class="cycle-pill"><strong>10 days</strong> left in your billing cycle</div>
      </div>
      <div class="preview-tips">
        <p class="tips-heading">Things you can do right now to lower your risk of high energy bills.</p>
        <div class="tips">
          <div class="tip">
            <div class="tip-icon" role="img" aria-label="Icon of household members talking"></div>
            <p class="tip-title">Inform the Household</p>
            <p class="tip-body">Inform everyone in the household of the need to save energy this month. Team work makes the dream work!</p>
            <div class="tip-button">I Did It</div>
          </div>
          <div class="tip">
            <div class="tip-icon" role="img" aria-label="Icon of a sleeping laptop"></div>
            <p class="tip-title">Enable Power-Save Modes</p>
            <p class="tip-body">Many electronics have power save modes that you can enable to lower consumption when they're not in use.</p>
            <div class="tip-button">I Did It</div>
          </div>
          <div class="tip">
            <div class="tip-icon" role="img" aria-label="Icon of a washing machine and thermometer"></div>
            <p class="tip-title">Cold cycle your laundry</p>
            <p class="tip-body">Did you know that running your washer on a cold cycle will lower reduce consumption of electricity or gas?</p>
            <div class="tip-button">I Did It</div>
          </div>
        </div>
      </div>
    </section>

    <div class="brand-disc"></div>

    <p class="benefit">Never get the bad surprise of a high<br>energy bill again with Lumo Signal.</p>
    <p class="benefit">Our email alerts will put you in<br>control of your energy usage</p>
    <p class="benefit">Get your alerts on the go by email<br>or SMS so you're always in control</p>
    <p class="benefit">Save on your energy expenses with our<br>simple and easy timely recommendations</p>

    <div class="contact">
      <span>
        <svg width="22" height="22" viewBox="0 0 24 24" aria-hidden="true"><circle cx="12" cy="12" r="10.5" fill="none" stroke="#fff" stroke-width="2"/><path d="M8.5 6.5c-1 1-1 3 1 6s4 5 5.5 4.5l1.2-1.3-2-2-1.2.8c-1-.5-2.6-2.3-3-3.4l.8-1.2-2-2z" fill="#fff"/></svg>
        000-000-0000
      </span>
      <span>
        <svg width="20" height="20" viewBox="0 0 24 24" aria-hidden="true" fill="none" stroke="#fff" stroke-width="2"><circle cx="12" cy="12" r="10"/><ellipse cx="12" cy="12" rx="4.5" ry="10"/><path d="M2 12h20"/></svg>
        www.lumocrest.example
      </span>
    </div>

    <p class="brand-name">LUMO SIGNAL</p>
  </main>
</body>
</html>
```